Harborlight Capital Estates business card

We are a real estate advisory and investment company. We are specialized in assisting high networth individuals to invest in real estate overseas. We deliver a very personalized service, anticipating all the potential challenges an investor can face, and making it easy and safe for them. We also co-invest with our clients, assuring them that each project will be looked after as it is our own, and at the same time giving them the extra booth on confidence to invest.

We need a business card design. The business card must have a very premium, high-end look, reflecting principles like "commitment", "trust" and "timeless (but contemporary)". We look for long term relationships with our clients, and we grow with their referrals. We are all about conquering the confidence of the clients by always delivering above the expectations performance.

Target Market(s)

High net worth individuals.

Industry/Entity Type

Real Estate

Contact Information for Business Card

Please consider places on the business card for:

Name
Function (bellow name in smaller size text)

Mobile phone
E-mail
Skype ID
WeChat ID

Adress (3 lines)

Also include the following locations references:
PORTUGAL * DUBAI * HONG KONG

Website: www.hcestates-example.com

Requirements
Must have
• Company Logo

```html
<!DOCTYPE html>
<html lang="en">
<head>
<meta charset="utf-8">
<title>Harborlight Capital Estates – Business Card</title>
<link rel="stylesheet" href="https://fonts.googleapis.com/css2?family=Cinzel:wght@400&family=PT+Sans:wght@400;700&display=swap">
<style>
  :root {
    --backdrop: #2b2b2e;
    --brand-blue: #2aa9e1;
    --paper: #ffffff;
    --ink-grey: #6d6e71;
    --swoosh-grey: #9a9b9e;
  }
  * { box-sizing: border-box; margin: 0; padding: 0; }
  html, body {
    width: 1200px; height: 925px; overflow: hidden;
    background: var(--backdrop);
    font-family: "PT Sans", Arial, sans-serif;
  }
  .canvas {
    position: relative; width: 1200px; height: 925px;
    display: flex; align-items: center; justify-content: center; gap: 40px;
  }
  .card {
    position: relative; width: 530px; height: 303px; overflow: hidden;
    box-shadow: 0 10px 28px rgba(0,0,0,.45);
  }

  /* Front */
  .card--front { background: var(--brand-blue); color: var(--paper); }
  .front__name {
    position: absolute; left: 0; right: 0; top: 108px;
    text-align: center; font-family: "Cinzel", Georgia, serif;
    font-size: 30px; line-height: 1.15; letter-spacing: 1px;
  }
  .front__name span { display: block; font-size: 17px; letter-spacing: 5px; margin-top: 4px; }
  .front__locations {
    position: absolute; right: 34px; bottom: 28px;
    font-size: 15px; letter-spacing: .3px;
  }

  /* Back */
  .card--back { background: var(--paper); color: var(--ink-grey); }
  .back__swoosh { position: absolute; inset: 0; width: 530px; height: 303px; }
  .back__person { position: absolute; right: 34px; top: 30px; text-align: right; }
  .person__name { color: var(--brand-blue); font-weight: 700; font-size: 17px; letter-spacing: .5px; }
  .person__role { font-size: 15px; margin-top: 1px; }
  .back__address {
    position: absolute; right: 34px; top: 100px; text-align: right;
    font-size: 12.5px; line-height: 1.35;
  }
  .back__name {
    position: absolute; left: 30px; top: 118px; color: var(--brand-blue);
    font-family: "Cinzel", Georgia, serif; font-size: 21px; line-height: 1.15;
  }
  .back__name span { display: block; font-size: 12px; letter-spacing: 3.5px; margin-top: 3px; }
  .back__contacts {
    position: absolute; left: 30px; top: 196px; list-style: none;
    font-size: 14px; line-height: 1.3;
  }
  .contact { display: flex; align-items: center; gap: 5px; }
  .contact__icon {
    width: 12px; height: 12px; border-radius: 2px; background: var(--brand-blue);
    display: inline-flex; align-items: center; justify-content: center;
  }
  .contact__icon--chat { background: #5fb236; border-radius: 50%; }
  .back__website {
    position: absolute; right: 22px; bottom: 12px;
    color: var(--paper); font-size: 13px;
  }
</style>
</head>
<body>
<main class="canvas">

  <section class="card card--front" aria-label="Business card front">
    <h1 class="front__name">Harborlight<span>Capital Estates</span></h1>
    <p class="front__locations">Portugal • Dubai • Hong Kong</p>
  </section>

  <section class="card card--back" aria-label="Business card back">
    <svg class="back__swoosh" viewBox="0 0 530 303" aria-hidden="true">
      <path d="M170 303 C290 288 390 205 505 150 L530 140 L530 215 C420 238 320 288 210 303 Z" fill="var(--swoosh-grey)"/>
      <path d="M205 303 C320 290 420 245 530 212 L530 303 Z" fill="var(--brand-blue)"/>
    </svg>

    <div class="back__person">
      <p class="person__name">DANIEL REYES</p>
      <p class="person__role">President</p>
    </div>

    <address class="back__address" style="font-style:normal">
      N. 8 Harbor Lane,<br>Suite 200, Lakeview,<br>WA 00000
    </address>

    <p class="back__name">Harborlight<span>Capital Estates</span></p>

    <ul class="back__contacts">
      <li class="contact">
        <span class="contact__icon">
          <svg width="8" height="8" viewBox="0 0 10 10" aria-hidden="true"><path d="M2 1 L4 1 L4.6 3.2 L3.5 4 C4 5.2 4.8 6 6 6.5 L6.8 5.4 L9 6 L9 8 C5 8.5 1.5 5 2 1 Z" fill="#fff"/></svg>
        </span>555.010.2468
      </li>
      <li class="contact">
        <span class="contact__icon">
          <svg width="8" height="8" viewBox="0 0 10 10" aria-hidden="true"><rect x="1" y="2.5" width="8" height="5.5" fill="none" stroke="#fff" stroke-width="1"/><path d="M1 2.5 L5 5.5 L9 2.5" fill="none" stroke="#fff" stroke-width="1"/></svg>
        </span>info@hcestates-example.com
      </li>
      <li class="contact"><span class="contact__icon"></span>/hcEstates</li>
      <li class="contact"><span class="contact__icon contact__icon--chat"></span>/hcEstates</li>
    </ul>

    <p class="back__website">www.hcestates-example.com</p>
  </section>

</main>
</body>
</html>
```